Income Tax Flyer - Updates Needed

Just need to update this flyer design and give it a new look. We would like to keep all the same wording but make it stand out a little more. Our selling point is the "Same Day Tax Advance up to $6,000"

Industry/Entity Type

Lending, Small Loans, Tax Services, Title Loans, Personal Loans

```html
<!DOCTYPE html>
<html lang="en">
<head>
<meta charset="utf-8">
<title>Keystone Lending Group – Same Day Tax Advance Flyer</title>
<link href="https://fonts.googleapis.com/css2?family=Arimo:wght@400;700&display=swap" rel="stylesheet">
<style>
  :root {
    --brand-red: #d0202a;
    --brand-red-dark: #a8161f;
    --brand-green: #0f5228;
    --brand-green-dark: #0a3d1d;
    --ink: #1b1b1b;
    --paper: #f4f4f2;
    --paper-shade: #e6e6e3;
    --card: #ffffff;
    --white: #ffffff;
  }
  * { margin: 0; padding: 0; box-sizing: border-box; }
  html, body { width: 950px; height: 1200px; overflow: hidden; background: var(--paper); }
  body { font-family: "Arimo", Arial, sans-serif; color: var(--ink); }

  .flyer { position: relative; width: 950px; height: 1200px; overflow: hidden;
    background: linear-gradient(170deg, var(--paper) 45%, var(--paper-shade) 100%); }
  .flyer-shapes { position: absolute; inset: 0; }

  .brand { position: absolute; left: 50px; top: 46px; display: flex; align-items: center; gap: 10px;
    padding: 12px 22px; background: var(--white); border-radius: 40px;
    font-weight: 700; font-size: 26px; line-height: 1; color: var(--brand-green); }
  .brand-dot { width: 16px; height: 16px; border-radius: 50%; background: var(--brand-red); }

  .selling-point { position: absolute; left: 95px; width: 760px; top: 392px; height: 124px;
    background: var(--brand-green); border-radius: 16px; border-bottom: 6px solid var(--brand-red);
    display: flex; flex-direction: column; align-items: center; justify-content: center; gap: 8px; }
  .selling-tag { background: var(--brand-red); color: var(--white); font-weight: 700; font-size: 22px;
    letter-spacing: 3px; line-height: 1; padding: 7px 20px; border-radius: 20px; }
  .selling-line { color: var(--white); font-weight: 700; font-size: 42px; line-height: 1; letter-spacing: 0.5px; }
  .selling-line .amount { color: #ffd9db; }

  .headline { position: absolute; left: 0; right: 0; top: 548px; text-align: center;
    font-weight: 700; font-size: 52px; line-height: 60px; color: var(--brand-green); }
  .headline .amount { color: var(--brand-red); }

  .subline { position: absolute; left: 0; right: 0; top: 684px; text-align: center;
    font-size: 34px; line-height: 42px; color: var(--ink); }
  .subline strong { font-weight: 700; }

  .features { position: absolute; left: 110px; right: 110px; top: 806px; display: flex; justify-content: space-between; }
  .feature { width: 225px; height: 196px; background: var(--card); border-radius: 16px;
    border-top: 5px solid var(--brand-red); box-shadow: 0 6px 18px rgba(0,0,0,0.08);
    display: flex; flex-direction: column; align-items: center; justify-content: center; text-align: center; }
  .feature svg { display: block; height: 70px; margin-bottom: 16px; }
  .feature-label { font-weight: 700; font-size: 20px; line-height: 24px; color: var(--ink); }

  .contact-title { position: absolute; left: 54px; top: 1040px; font-weight: 700; font-size: 26px; line-height: 30px; color: var(--ink); }
  .contact-phone { position: absolute; left: 54px; top: 1096px; height: 72px; display: flex; align-items: center; gap: 20px;
    font-weight: 700; font-size: 52px; line-height: 1; color: var(--white); }
  .address { position: absolute; left: 712px; top: 1074px; font-size: 21px; line-height: 27px; color: var(--white); font-style: normal; }
</style>
</head>
<body>
<main class="flyer">
  <svg class="flyer-shapes" width="950" height="1200" viewBox="0 0 950 1200">
    <defs>
      <linearGradient id="office-photo-tones" x1="0" y1="0" x2="1" y2="1">
        <stop offset="0" stop-color="#ebe8e3"/>
        <stop offset="0.5" stop-color="#d9d5cf"/>
        <stop offset="1" stop-color="#c8c3bd"/>
      </linearGradient>
    </defs>
    <path role="img" aria-label="Photo: two smiling women talking across a desk in a bright office"
          d="M0 0 H950 V330 C760 420 560 440 475 440 C390 440 190 420 0 330 Z" fill="url(#office-photo-tones)"/>
    <path class="swoosh" d="M0 330 C190 420 390 440 475 440 C560 440 760 420 950 330 V356 C760 448 560 466 475 466 C390 466 190 448 0 356 Z" fill="var(--brand-red)"/>
    <circle cx="1010" cy="620" r="95" fill="var(--brand-red)"/>
    <circle cx="-40" cy="760" r="100" fill="var(--brand-green)"/>
    <path class="phone-band" d="M0 1096 H606 L566 1168 H0 Z" fill="var(--brand-red)"/>
    <path class="address-block" d="M646 1050 H950 V1200 H554 L630 1064 Q636 1050 646 1050 Z" fill="var(--brand-green)"/>
  </svg>

  <div class="brand"><span class="brand-dot"></span>Keystone Lending Group</div>

  <section class="selling-point">
    <span class="selling-tag">SAME DAY</span>
    <p class="selling-line">TAX ADVANCE UP TO <span class="amount">$6,000</span></p>
  </section>

  <h1 class="headline">APPLY HERE FOR<br><span class="amount">$5,000 - $ 6,000</span> TODAY!</h1>
  <p class="subline">File your taxes and apply<br>for <strong>an Easy Advance!</strong></p>

  <section class="features">
    <div class="feature">
      <svg viewBox="0 0 70 82" width="60" fill="none" stroke="var(--brand-red)" stroke-width="3.5" stroke-linejoin="round">
        <path d="M24 4 L35 12 L46 4 L42 20 H28 Z"/>
        <path d="M28 20 C10 30 2 48 4 62 C6 76 20 79 35 79 C50 79 64 76 66 62 C68 48 60 30 42 20"/>
        <text x="35" y="62" text-anchor="middle" font-family="Arimo, sans-serif" font-size="24" font-weight="700" fill="var(--brand-red)" stroke="none">$</text>
      </svg>
      <p class="feature-label">Choose your<br>Loan Amount</p>
    </div>
    <div class="feature">
      <svg viewBox="0 0 82 82" width="70" fill="none" stroke="var(--brand-red)" stroke-width="3.5" stroke-linecap="round">
        <circle cx="41" cy="41" r="38"/>
        <path d="M66 50 A27 27 0 1 1 66 32"/>
        <path d="M60 56 L66 50 L70 58"/>
        <path d="M41 26 V41 L52 48"/>
        <circle cx="41" cy="41" r="3" fill="var(--brand-red)"/>
      </svg>
      <p class="feature-label">Available in<br>24 Hours or Less</p>
    </div>
    <div class="feature">
      <svg viewBox="0 0 52 82" width="44" fill="none" stroke="var(--brand-red)" stroke-width="3.5" stroke-linecap="round">
        <rect x="3" y="3" width="46" height="76" rx="6"/>
        <path d="M3 14 H49 M3 66 H49 M20 8 H32"/>
        <path d="M15 38 A11 11 0 0 1 36 34 M37 44 A11 11 0 0 1 16 48"/>
        <path d="M32 30 L36 34 L40 29 M20 52 L16 48 L12 53"/>
      </svg>
      <p class="feature-label">Quick and<br>Easy</p>
    </div>
  </section>

  <p class="contact-title">CONTACT US TODAY!</p>
  <div class="contact-phone">
    <svg width="38" height="38" viewBox="0 0 24 24" fill="var(--white)" aria-hidden="true">
      <path d="M6.6 10.8a15.1 15.1 0 0 0 6.6 6.6l2.2-2.2a1 1 0 0 1 1-.25 11.4 11.4 0 0 0 3.6.57 1 1 0 0 1 1 1V20a1 1 0 0 1-1 1A17 17 0 0 1 3 4a1 1 0 0 1 1-1h3.5a1 1 0 0 1 1 1c0 1.25.2 2.45.57 3.57a1 1 0 0 1-.25 1z"/>
    </svg>
    <span>012 555 0184</span>
  </div>
  <address class="address">Address Line 1<br>Address Line 2<br>Address Line 3</address>
</main>
</body>
</html>
```